Real Estate Investment Company Needs A Business Card Designed

I need a business card designed for my use. We are a real estate investment company based in Omaha, Nebraska that specializes in buying, rehabbing and selling single family and multifamily properties. Would love designs that incorporate our logo and colors

Industry/Entity Type

Business

Contact Information for Business Card

Marlow Pettigrew | President & CEO
4837 North 52nd Avenue, Ste 200
Omaha, NE 68214
(402) 555-7428
marlow@quillfenhomes.example
www.QuillfenHomes.example

Font styles to use
Serif

Colors
0255a3
3276b5

Requirements
Must have
• Our logo

```html
<!DOCTYPE html>
<html lang="en">
<head>
<meta charset="utf-8">
<title>Quillfen Homes — Business Card</title>
<link href="https://fonts.googleapis.com/css2?family=Jost:wght@600&family=Roboto:wght@400&display=swap" rel="stylesheet">
<style>
  :root {
    --backdrop: #3b3b3d;
    --card: #1e1f23;
    --brand-blue: #2f86d0;
    --brand-blue-light: #4fa3df;
    --silver: #c9cacc;
    --white: #f4f5f6;
  }
  * { margin: 0; padding: 0; box-sizing: border-box; }
  html, body {
    width: 799px;
    height: 1200px;
    overflow: hidden;
    background: var(--backdrop);
  }
  .stage {
    width: 799px;
    height: 1200px;
    display: flex;
    flex-direction: column;
    align-items: center;
    justify-content: space-around;
    padding: 60px 0;
  }
  .card {
    position: relative;
    width: 640px;
    height: 366px;
    background: var(--card);
    border-radius: 3px;
    box-shadow: 0 14px 30px rgba(0,0,0,0.45);
    overflow: hidden;
    font-family: "Roboto", Arial, sans-serif;
    color: var(--white);
  }
  .brand {
    display: flex;
    align-items: center;
    gap: 18px;
    font-family: "Jost", "Futura", sans-serif;
    font-weight: 600;
    color: var(--brand-blue);
    text-transform: uppercase;
    letter-spacing: 0.02em;
    white-space: nowrap;
  }
  .brand-dot {
    border-radius: 50%;
    background: var(--brand-blue);
    flex: none;
  }
  .card-front .brand {
    position: absolute;
    left: 50%;
    top: 50%;
    transform: translate(-50%, -50%);
    font-size: 44px;
  }
  .card-front .brand-dot { width: 96px; height: 96px; }
  .card-back .brand {
    position: absolute;
    left: 34px;
    top: 34px;
    font-size: 40px;
  }
  .card-back .brand-dot { width: 92px; height: 92px; }
  .holder {
    position: absolute;
    left: 34px;
    top: 196px;
  }
  .holder-name {
    font-family: "Jost", sans-serif;
    font-weight: 600;
    font-size: 26px;
    color: var(--brand-blue);
    line-height: 1.1;
  }
  .holder-title {
    font-size: 14px;
    color: var(--white);
    margin-top: 2px;
  }
  .bands {
    position: absolute;
    left: 0;
    top: 0;
  }
  .contact {
    position: absolute;
    left: 372px;
    top: 176px;
    font-size: 15px;
    line-height: 1.3;
  }
  .contact-row {
    display: flex;
    align-items: center;
    gap: 8px;
  }
  .contact-address { margin-bottom: 4px; }
  .contact-icon { width: 14px; height: 14px; flex: none; fill: var(--brand-blue); }
  .website {
    position: absolute;
    right: 30px;
    bottom: 22px;
    font-size: 16px;
    color: var(--white);
  }
</style>
</head>
<body>
<main class="stage">

  <section class="card card-front" aria-label="Card front">
    <div class="brand">
      <span class="brand-dot"></span>
      <span class="brand-name">Quillfen Homes</span>
    </div>
  </section>

  <section class="card card-back" aria-label="Card back">
    <svg class="bands" width="640" height="366" viewBox="0 0 640 366" aria-hidden="true">
      <defs>
        <linearGradient id="blue-band" x1="0" y1="0" x2="1" y2="0">
          <stop offset="0" stop-color="#2277c4"/>
          <stop offset="1" stop-color="#52a6e0"/>
        </linearGradient>
        <linearGradient id="silver-band" x1="0" y1="0" x2="1" y2="0">
          <stop offset="0" stop-color="#e6e7e8"/>
          <stop offset="1" stop-color="#b9babd"/>
        </linearGradient>
      </defs>
      <polygon points="0,268 300,268 272,308 0,308" fill="url(#silver-band)"/>
      <polygon points="312,268 640,268 640,366 256,366" fill="url(#blue-band)"/>
    </svg>

    <div class="brand">
      <span class="brand-dot"></span>
      <span class="brand-name">Quillfen Homes</span>
    </div>

    <div class="holder">
      <p class="holder-name">Marlow Pettigrew</p>
      <p class="holder-title">President &amp; CEO</p>
    </div>

    <div class="contact">
      <p class="contact-address">4837 North 52nd Avenue, Ste 200<br>Omaha, NE 68214</p>
      <p class="contact-row">
        <svg class="contact-icon" viewBox="0 0 24 24" aria-hidden="true"><path d="M6.6 10.8a15.1 15.1 0 0 0 6.6 6.6l2.2-2.2a1 1 0 0 1 1-.25 11.4 11.4 0 0 0 3.6.57 1 1 0 0 1 1 1V20a1 1 0 0 1-1 1A17 17 0 0 1 3 4a1 1 0 0 1 1-1h3.5a1 1 0 0 1 1 1c0 1.25.2 2.45.57 3.57a1 1 0 0 1-.25 1z"/></svg>
        (402) 555-7428
      </p>
      <p class="contact-row">
        <svg class="contact-icon" viewBox="0 0 24 24" aria-hidden="true"><path d="M2 5h20v14H2z M3.5 6.5 12 13l8.5-6.5" stroke="#1e1f23" stroke-width="1.6"/></svg>
        marlow@quillfenhomes.example
      </p>
    </div>

    <p class="website">www.QuillfenHomes.example</p>
  </section>

</main>
</body>
</html>
```